Psychologist Banner Ads for Remarketing & yarnwave

Brand awareness campaign for tallowbridge.com.au

// Ad Formats //
Static JPEG
Max 45KB in file size
All ads must have a border

// Ad Sizes //
Static: (for Zindle Display network) 300×250, 160×600, 728×90
Static: (for Yarnwave, no more than 25% text): 600×315, 1200 x 627

Please use logo, image and "maximise your wellbeing" from the website home page.

```html
<!DOCTYPE html>
<html lang="en">
<head>
<meta charset="utf-8">
<title>Tallowbridge Psychology – Display Banners</title>
<link rel="stylesheet" href="https://fonts.googleapis.com/css2?family=Arimo:ital,wght@0,400;1,700&display=swap">
<style>
  :root {
    --page-bg: #ffffff;
    --banner-border: #cdd8dd;
    --brand-blue-light: #0ea3cc;
    --brand-blue: #0b86b4;
    --brand-blue-deep: #0a6692;
    --sky-light: #f1f9fb;
    --sky-mid: #cfe9f1;
    --skin-warm: #d9b8a4;
    --logo-ink: #1c4f97;
    --logo-card: #ffffff;
    --tagline: #ffffff;
  }

  * { box-sizing: border-box; margin: 0; padding: 0; }

  html, body {
    width: 1200px;
    height: 1155px;
    overflow: hidden;
    background: var(--page-bg);
  }

  .canvas {
    position: relative;
    width: 1200px;
    height: 1155px;
  }

  .banner {
    position: absolute;
    overflow: hidden;
    border: 1.5px solid var(--banner-border);
    background:
      linear-gradient(155deg, var(--brand-blue-light) 0%, var(--brand-blue) 45%, var(--brand-blue-deep) 100%);
  }

  .banner__photo {
    position: absolute;
    left: 0;
    top: 0;
    background:
      radial-gradient(ellipse 45% 60% at 40% 55%, rgba(217,184,164,0.55) 0%, rgba(217,184,164,0) 70%),
      linear-gradient(180deg, var(--sky-mid) 0%, var(--sky-light) 100%);
  }

  .logo-card {
    position: absolute;
    width: 206px;
    height: 117px;
    background: var(--logo-card);
    box-shadow: 0 2px 6px rgba(0,0,0,0.25);
    display: flex;
    flex-direction: column;
    align-items: flex-start;
    justify-content: center;
    padding: 0 14px;
    font-family: "Arimo", Arial, sans-serif;
    font-weight: 400;
    color: var(--logo-ink);
  }

  .logo-card__name {
    font-size: 31px;
    line-height: 1.05;
    letter-spacing: -0.3px;
  }

  .logo-card__field {
    font-size: 19px;
    letter-spacing: 2.4px;
    margin-top: 6px;
  }

  .tagline {
    position: absolute;
    font-family: "Arimo", Arial, sans-serif;
    font-style: italic;
    font-weight: 700;
    color: var(--tagline);
    text-shadow: 0 1px 3px rgba(0,0,0,0.3);
    text-align: center;
    white-space: nowrap;
  }

  /* 160 × 600 skyscraper */
  .banner--skyscraper { left: 18px; top: 16px; width: 253px; height: 957px; }
  .banner--skyscraper .banner__photo { width: 100%; height: 360px; }
  .banner--skyscraper .logo-card { left: 26px; top: 336px; }
  .banner--skyscraper .tagline {
    left: 0; right: 0; top: 620px;
    font-size: 38px;
    line-height: 48px;
    white-space: normal;
  }

  /* 300 × 250 rectangle */
  .banner--rectangle { left: 290px; top: 576px; width: 477px; height: 397px; }
  .banner--rectangle .banner__photo { width: 100%; height: 192px; }
  .banner--rectangle .logo-card { left: 136px; top: 168px; }
  .banner--rectangle .tagline {
    left: 0; right: 0; top: 323px;
    font-size: 28px;
    line-height: 36px;
  }

  /* 728 × 90 leaderboard */
  .banner--leaderboard { left: 18px; top: 992px; width: 1162px; height: 142px; }
  .banner--leaderboard .banner__photo { width: 582px; height: 100%; }
  .banner--leaderboard .logo-card { left: 531px; top: 10px; }
  .banner--leaderboard .tagline {
    left: 770px; width: 350px; top: 53px;
    font-size: 27px;
    line-height: 34px;
  }
</style>
</head>
<body>
<main class="canvas">

  <section class="banner banner--skyscraper" aria-label="160 by 600 banner">
    <div class="banner__photo" role="img" aria-label="Photo of a joyful woman laughing with arms raised against a pale blue sky"></div>
    <div class="logo-card">
      <span class="logo-card__name">Tallowbridge</span>
      <span class="logo-card__field">PSYCHOLOGY</span>
    </div>
    <p class="tagline">maximise<br>your<br>wellbeing</p>
  </section>

  <section class="banner banner--rectangle" aria-label="300 by 250 banner">
    <div class="banner__photo" role="img" aria-label="Photo of a joyful woman laughing with arms raised against a pale blue sky"></div>
    <div class="logo-card">
      <span class="logo-card__name">Tallowbridge</span>
      <span class="logo-card__field">PSYCHOLOGY</span>
    </div>
    <p class="tagline">maximise your wellbeing</p>
  </section>

  <section class="banner banner--leaderboard" aria-label="728 by 90 banner">
    <div class="banner__photo" role="img" aria-label="Photo of a joyful woman laughing with arms outstretched against a pale blue sky"></div>
    <div class="logo-card">
      <span class="logo-card__name">Tallowbridge</span>
      <span class="logo-card__field">PSYCHOLOGY</span>
    </div>
    <p class="tagline">maximise your wellbeing</p>
  </section>

</main>
</body>
</html>
```